A colorful, playful, nerdy, creative logo for a business analytics and marketing analytics company.

We need a logo and website design for a new company based in Florida called Brightfold Pattern Works Collective. We provide marketing, consumer and business insights through the use of market research, business analytics and marketing analytics. We are a collection of several individuals each with specific expertise and come together to provide the best possible insights about their consumers/guests/customers. We would like to see a design that uses colors that show a free spirit but deeply rooted in analytics " a super nerd " Along those steps, we would like to see either a playful, nerdy, creative logo or one that includes the full or partial name of the company. We have simplified our "brand" by saying when you initially start with us you may have several questions "?" through the process of learning about your consumers/brand ">" incredible solutions, strategies are developed "!" So something like a ?>! symbol would be interesting. Although the name of the company sounds very complex and very long to write, we would be interested in thoughtful ways of shorting the name or incorporating into the final logo design

Target Market(s)

Business or organizations that currently do not have an analytics/research function

Industry/Entity Type

Business

Contact Information for Business Card

Incorporate final logo and colors font. In the past, I have used a "wordle" website to show 10 common research terms scattered about .. showing them as strength or core competencies.

Logo Text

?>! or Brightfold Pattern Works Collective or BPW Collective

Coding

Coded - Design and coding required

Number of Pages Required

4 page

Font styles to use
Sans Serif
Decorative

Requirements
Must have
• The project must communicate analytics/scientific. It must we unique but not unique for the sack of being unique.
• It must either be a logo or a simple way to communicate the company name Brightfold Pattern Works Collective
Nice to have
• Again incorporating the symbols ?>! in that order. Showing confusion to gaining insights and then developing incredible solutions that are used to effect consumer behavior.
• Look to CPG ( consumer package goods) industry to input
Should not have
• I am pretty open to suggestions.

```html
<!DOCTYPE html>
<html lang="en">
<head>
<meta charset="utf-8">
<title>Brightfold Pattern Works Collective</title>
<link rel="stylesheet" href="https://fonts.googleapis.com/css2?family=Montserrat:wght@400;500;600;700&family=Roboto+Condensed:wght@400;700&display=swap">
<style>
:root{
  --blue:#1c5d8d;
  --blue-dark:#164a72;
  --orange:#f4a21c;
  --ink:#2f2f2f;
  --muted:#555;
  --gray-bg:#efefef;
  --outer:#e6e6e6;
  --white:#fff;
  --ring1:#9c9c9c;
  --ring2:#cdcdcd;
  --ring3:#b3b3b3;
}
*{box-sizing:border-box;margin:0;padding:0}
html,body{width:1200px;height:3557px;overflow:hidden}
body{background:var(--outer);font-family:'Montserrat',sans-serif;color:var(--ink);position:relative}
section,header,footer{position:absolute;left:14px;width:1172px}

/* header */
.site-header{top:0;height:166px;background:var(--white)}
.topbar{position:absolute;right:0;top:12px;width:426px;height:40px;background:var(--blue);color:var(--white);font-size:12px;font-weight:600;display:flex;align-items:center;gap:22px;padding-left:40px;clip-path:polygon(6% 0,100% 0,100% 100%,0 100%)}
.topbar .item{display:flex;align-items:center;gap:7px}
.social{display:flex;gap:6px}
.social span{width:12px;height:12px;background:var(--white);border-radius:2px;display:block}
.brand{position:absolute;left:32px;top:70px;display:flex;align-items:center;gap:10px;font-size:17px;font-weight:700;color:var(--blue)}
.brand .dot{width:22px;height:22px;border-radius:50%;background:var(--orange)}
.main-nav{position:absolute;top:102px;left:410px;display:flex}
.main-nav a{font-family:'Roboto Condensed',sans-serif;font-size:14px;color:var(--ink);text-decoration:none;text-transform:uppercase;padding:0 16px;display:flex;align-items:center;gap:7px;border-left:1px solid #ddd;height:24px}
.main-nav a:first-child{border-left:0}
.main-nav a.active{color:var(--orange)}
.main-nav svg{width:16px;height:16px}

/* hero */
.hero{top:166px;height:557px;background:linear-gradient(180deg,#dfe6ef 0%,#b8b0cc 30%,#6f6a92 55%,#c9c7d8 78%,#f1f1f4 100%)}
.hero-dots{position:absolute;left:530px;bottom:22px;display:flex;gap:10px}
.hero-dots span{width:22px;height:4px;background:#fff;opacity:.7}
.hero-dots span.on{background:var(--orange);opacity:1}
.intro{top:723px;height:221px;background:linear-gradient(180deg,#e2e2e2,#cfcfcf);text-align:center;box-shadow:0 6px 10px rgba(0,0,0,.12)}
.intro p{width:980px;margin:42px auto 0;font-size:16.5px;line-height:23px;color:#333}
.btn{display:inline-flex;align-items:center;justify-content:center;font-size:14px;font-weight:700;letter-spacing:1px;text-transform:uppercase}
.btn-solid{position:absolute;left:436px;top:140px;width:302px;height:38px;background:var(--blue-dark);color:#fff;border-radius:3px}
.btn-outline{position:absolute;width:302px;height:40px;border:2px solid var(--blue);color:var(--blue);border-radius:6px;background:#fff}

/* section headings */
.section-title{position:absolute;left:0;width:1172px;display:flex;justify-content:center;align-items:center;gap:14px;font-family:'Roboto Condensed',sans-serif;font-weight:700;font-size:24px;text-transform:uppercase;color:var(--ink)}
.section-title::before,.section-title::after{content:"";width:70px;height:1px;background:#cfcfcf}
.section-title .mark{width:14px;height:14px;border-radius:50%;background:var(--orange)}
.section-title em{font-style:normal;color:var(--blue)}
.on-dark{color:#fff}
.on-dark em{color:var(--orange)}
.on-dark::before,.on-dark::after{background:rgba(255,255,255,.5)}
.body-copy{font-size:13.5px;line-height:19px;color:var(--muted)}

/* who we are */
.who{top:944px;height:431px;background:var(--white)}
.who .copy{position:absolute;left:45px;top:128px;width:690px}
.who .copy p+p{margin-top:19px}
.video{position:absolute;left:776px;top:130px;width:350px;height:185px;background:linear-gradient(120deg,#7b2f36,#c9b6b0 45%,#6a4a52);box-shadow:0 6px 14px rgba(0,0,0,.3)}
.play{position:absolute;left:140px;top:57px;width:70px;height:70px;border-radius:50%;background:rgba(255,255,255,.85)}
.play::after{content:"";position:absolute;left:28px;top:21px;border-left:22px solid #555;border-top:14px solid transparent;border-bottom:14px solid transparent}

/* what we do */
.what{top:1375px;height:635px;background:var(--gray-bg)}
.what .lead{position:absolute;top:126px;width:100%;text-align:center;font-size:13.5px;font-weight:600;color:#333}
.rings{position:absolute;left:0;top:165px}
.service{position:absolute;top:27px;width:246px;height:246px;border-radius:50%;background:#fff;text-align:center;padding:70px 30px 0}
.service svg{position:absolute;left:93px;top:20px;width:60px;height:60px}
.service p{font-size:13.5px;line-height:18px;color:var(--muted)}

/* expertise */
.expertise{top:2010px;height:513px;background:linear-gradient(110deg,#2a6ea6 0%,#3d85c0 40%,#2f6ea4 70%,#7fb4df 100%)}
.expertise .veil{position:absolute;inset:0;background:linear-gradient(180deg,rgba(18,70,120,.35),rgba(18,70,120,.15))}
.orbit{position:absolute;left:0;top:0}
.exp-item{position:absolute;color:#fff}
.exp-item h3{font-size:13px;font-weight:700;text-transform:uppercase;letter-spacing:.5px}
.exp-item p{font-size:13px;line-height:17px;color:#eaf2fa}
.center-name{position:absolute;left:502px;top:325px;width:200px;text-align:center;font-size:17px;font-weight:700;color:#fff}

/* news */
.news{top:2523px;height:524px;background:var(--gray-bg)}
.card{position:absolute;top:132px;width:313px}
.card .photo{height:185px;border-radius:4px;box-shadow:0 4px 8px rgba(0,0,0,.25)}
.card .meta{margin-top:30px;font-size:13px;line-height:19px;color:#444;text-transform:uppercase}
.card .body-copy{margin-top:12px}

/* footer */
.site-footer{top:3047px;height:458px;background:#fff}
.notch{position:absolute;left:424px;top:-14px;width:324px;height:16px;background:#fff;clip-path:polygon(6% 0,94% 0,100% 100%,0 100%)}
.footer-brand{position:absolute;top:120px;width:100%;text-align:center;font-size:19px;font-weight:700;color:var(--blue)}
.footer-brand .dot{display:inline-block;width:24px;height:24px;border-radius:50%;background:var(--orange);vertical-align:middle;margin-right:10px}
.col{position:absolute;top:220px}
.col h4{font-size:13px;font-weight:700;color:var(--orange);text-transform:uppercase;letter-spacing:1px;padding-bottom:8px;border-bottom:1px solid #ddd;margin-bottom:14px;width:110px}
.col ul{list-style:none;font-size:12px;line-height:19px;color:#333}
.contact-row{display:flex;gap:14px;align-items:flex-start;font-size:12px;line-height:17px;font-weight:600;margin-bottom:16px}
.contact-row svg{width:20px;height:20px;flex:none}
.map{width:256px;height:166px;background:linear-gradient(135deg,#e9e4d8,#d6dccb 50%,#cfd8e0)}
.signup{display:flex;margin-top:4px}
.signup span{display:flex;align-items:center}
.signup .field{width:140px;height:36px;border:2px solid var(--blue);font-size:11px;font-weight:600;padding-left:8px}
.signup .go{width:87px;height:36px;background:var(--blue);color:#fff;font-size:12px;font-weight:700;justify-content:center}
.bottom-bar{position:absolute;left:14px;top:3505px;width:1172px;height:32px;background:var(--blue);color:#fff;font-size:11px;font-weight:600;display:flex;align-items:center;justify-content:space-between;padding:0 16px}
</style>
</head>
<body>

<header class="site-header">
  <div class="topbar">
    <span class="item"><svg width="14" height="10" viewBox="0 0 14 10"><rect width="14" height="10" fill="#fff"/><path d="M0 0l7 6 7-6" stroke="#1c5d8d" fill="none"/></svg>info@bpwcollective.com</span>
    <span class="item"><svg width="12" height="12" viewBox="0 0 12 12"><path d="M2 1l3 0 1 3-2 1c1 2 2 3 3 3l1-2 3 1v3c-6 0-9-4-9-9z" fill="#fff"/></svg>800-555-0147</span>
    <span class="social"><span></span><span></span><span></span><span></span></span>
  </div>
  <div class="brand"><span class="dot"></span>Brightfold Pattern Works Collective</div>
  <nav class="main-nav">
    <a class="active"><svg viewBox="0 0 16 16"><path d="M2 8l6-6 6 6M4 7v7h8V7" fill="none" stroke="#f4a21c" stroke-width="2"/></svg>Home</a>
    <a><svg viewBox="0 0 16 16"><rect x="3" y="2" width="10" height="13" fill="none" stroke="#333" stroke-width="1.5"/></svg>Who We Are</a>
    <a><svg viewBox="0 0 16 16"><path d="M2 14h12M4 12V6M8 12V3M12 12V8" stroke="#333" stroke-width="2"/></svg>What We Do</a>
    <a><svg viewBox="0 0 16 16"><circle cx="8" cy="8" r="6" fill="none" stroke="#333" stroke-width="1.5"/><circle cx="8" cy="8" r="2" fill="#333"/></svg>Expertise</a>
    <a><svg viewBox="0 0 16 16"><path d="M3 13L12 4M10 3l3 3" stroke="#333" stroke-width="2"/></svg>News</a>
    <a><svg viewBox="0 0 16 16"><path d="M3 2h3l1 4-2 1c1 2 2 3 4 4l1-2 4 1v3C8 13 3 8 3 2z" fill="#333"/></svg>Contact</a>
  </nav>
</header>

<section class="hero" role="img" aria-label="Photo of business people walking through a city street blended with skyline">
  <div class="hero-dots"><span class="on"></span><span></span><span></span></div>
</section>

<section class="intro">
  <p>We provide marketing, consumer and business insights through the use of market research, business analytics and marketing analytics. We are a collection of several individuals each with specific expertise and come together to provide the best possible insights about their consumers/guests/customers.</p>
  <span class="btn btn-solid">Get Started Today</span>
</section>

<section class="who">
  <h2 class="section-title" style="top:62px"><span class="mark"></span>Who <em>We Are</em></h2>
  <div class="copy body-copy">
    <p>Lorem ipsum dolor sit amet, consectetuer adipiscing elit, sed diam nonummy nibh euismod tincidunt ut laoreet dolore magna aliquam erat volutpat. Ut wisi enim ad minim veniam, quis nostrud exerci tation ullamcorper suscipit lobortis nisl ut aliquip ex ea commodo con sequat.</p>
    <p>Duis autem vel eum iriure dolor in hendrerit in vulputate velit esse molestie consequat, vel illum dolore eu feugiat nulla facilisis at vero eros et accumsan et iusto odio dignissim qui blandit praesent luptatum zzril delenit augue duis dolore te feugait nulla facilisi. Nam liber tempor cum soluta nobis eleifend option congue nihil imperdiet doming id quod mazim placerat facer possim assum.</p>
  </div>
  <span class="btn btn-outline" style="left:43px;top:334px">More About Us</span>
  <div class="video" role="img" aria-label="Video still of a city street with red brick buildings"><span class="play"></span></div>
</section>

<section class="what">
  <h2 class="section-title" style="top:62px"><span class="mark"></span>What <em>We Do</em></h2>
  <p class="lead">We provide marketing, consumer and business insights through the use of market research, business analytics and marketing analytics.</p>
  <svg class="rings" width="1172" height="330" viewBox="0 0 1172 330">
    <path d="M149 150 A145 145 0 0 1 439 150" fill="none" stroke="var(--ring1)" stroke-width="42"/>
    <path d="M438 150 A145 145 0 0 0 728 150" fill="none" stroke="var(--ring2)" stroke-width="42"/>
    <path d="M728 150 A145 145 0 0 1 1018 150" fill="none" stroke="var(--ring3)" stroke-width="42"/>
  </svg>
  <div class="rings" style="width:1172px;height:330px">
    <div class="service" style="left:171px">
      <svg viewBox="0 0 60 60"><path d="M10 24h8l20-12v36L18 36h-8z" fill="var(--orange)"/><path d="M16 36l4 14h6l-3-14" fill="var(--orange)"/><path d="M44 22l8-5M45 30h9M44 38l8 5" stroke="var(--orange)" stroke-width="3"/></svg>
      <p>Lorem ipsum dolor sit amet, consectetuer adipiscing elit, sed diam nonummy nibh euismod tincidunt ut laoreet dolore magna.</p>
    </div>
    <div class="service" style="left:460px">
      <svg viewBox="0 0 60 60"><circle cx="22" cy="8" r="6" fill="var(--orange)"/><path d="M16 16h10l4 16-6 0-2 22h-6l0-22z" fill="var(--orange)"/><path d="M28 30h26l-4 14H32z" fill="var(--orange)"/><circle cx="35" cy="50" r="3" fill="var(--orange)"/><circle cx="48" cy="50" r="3" fill="var(--orange)"/></svg>
      <p>Lorem ipsum dolor sit amet, consectetuer adipiscing elit, sed diam nonummy nibh euismod tincidunt ut laoreet dolore magna.</p>
    </div>
    <div class="service" style="left:749px">
      <svg viewBox="0 0 60 60"><text x="6" y="24" font-family="Montserrat,sans-serif" font-weight="700" font-size="24" fill="var(--orange)">$</text><rect x="20" y="40" width="8" height="16" fill="none" stroke="var(--orange)" stroke-width="3"/><rect x="32" y="30" width="8" height="26" fill="none" stroke="var(--orange)" stroke-width="3"/><rect x="44" y="20" width="8" height="36" fill="none" stroke="var(--orange)" stroke-width="3"/><path d="M22 26L40 10l6 3" stroke="var(--orange)" stroke-width="3" fill="none"/></svg>
      <p>Lorem ipsum dolor sit amet, consectetuer adipiscing elit, sed diam nonummy nibh euismod tincidunt ut laoreet dolore magna.</p>
    </div>
  </div>
  <span class="btn btn-outline" style="left:436px;top:543px">Learn More</span>
</section>

<section class="expertise" role="img" aria-label="Blue toned photo of a business person with charts and data screens">
  <div class="veil"></div>
  <h2 class="section-title on-dark" style="top:68px"><span class="mark"></span>Our <em>Expertise</em></h2>
  <svg class="orbit" width="1172" height="513" viewBox="0 0 1172 513">
    <circle cx="602" cy="335" r="150" fill="rgba(15,40,70,.35)" stroke="#fff" stroke-width="3"/>
    <g stroke="#fff" stroke-width="3" fill="#111">
      <circle cx="602" cy="185" r="46"/>
      <circle cx="469" cy="405" r="46"/>
      <circle cx="735" cy="405" r="46"/>
    </g>
    <path d="M582 203h42M585 200v-34M587 195l10-14 8 8 14-18" stroke="#fff" stroke-width="3" fill="none"/>
    <rect x="451" y="388" width="36" height="34" rx="5" fill="none" stroke="#fff" stroke-width="3"/>
    <circle cx="469" cy="405" r="8" fill="none" stroke="#fff" stroke-width="3"/>
    <rect x="716" y="388" width="38" height="26" fill="none" stroke="#fff" stroke-width="3"/>
    <path d="M735 414v8M726 424h18M724 408l8-8 6 4 10-10" stroke="#fff" stroke-width="3" fill="none"/>
  </svg>
  <div class="center-name">BPW Collective</div>
  <div class="exp-item" style="left:236px;top:130px;width:240px"><h3>Business Analytics</h3><p>Lorem ipsum dolor sit amet, consectetuer adipiscing elit, sed diam nonummy nibh euismod tincidunt ut laoreet dolore magna aliquam erat volutpat. Ut wisi enim ad minim veniam.</p></div>
  <div class="exp-item" style="left:97px;top:343px;width:290px"><h3>Market Research</h3><p>Lorem ipsum dolor sit amet, consectetuer adipiscing elit, sed diam nonummy nibh euismod tincidunt ut laoreet dolore magna aliquam erat volutpat. Ut wisi enim ad minim veniam.</p></div>
  <div class="exp-item" style="left:818px;top:343px;width:290px"><h3>Marketing Analytics</h3><p>Lorem ipsum dolor sit amet, consectetuer adipiscing elit, sed diam nonummy nibh euismod tincidunt ut laoreet dolore magna aliquam erat volutpat. Ut wisi enim ad minim veniam.</p></div>
</section>

<section class="news">
  <h2 class="section-title" style="top:64px"><span class="mark"></span>Latest <em>News</em></h2>
  <article class="card" style="left:93px">
    <div class="photo" role="img" aria-label="Photo of two business people shaking hands in an office" style="background:linear-gradient(135deg,#dfe3e8,#8e98a6 50%,#cfd5dc)"></div>
    <div class="meta">News #1<br>June 4, 2017</div>
    <p class="body-copy">Lorem ipsum dolor sit amet, consectetuer adipiscing elit, sed diam nonummy nibh euis mod tincidunt ut laoreet dolore magna ali quam erat volutpat.</p>
  </article>
  <article class="card" style="left:429px">
    <div class="photo" role="img" aria-label="Photo of office buildings and a road at dusk" style="background:linear-gradient(180deg,#1b3a66,#2f5e8c 45%,#3b4a3c 80%,#222)"></div>
    <div class="meta">News #2<br>June 4, 2017</div>
    <p class="body-copy">Lorem ipsum dolor sit amet, consectetuer adipiscing elit, sed diam nonummy nibh euis mod tincidunt ut laoreet dolore magna ali quam erat volutpat.</p>
  </article>
  <article class="card" style="left:766px">
    <div class="photo" role="img" aria-label="Photo of a businessman facing a wall of chalk sketched ideas" style="background:linear-gradient(180deg,#3d5d86,#6c87a8 50%,#2b3e58)"></div>
    <div class="meta">News #3<br>June 4, 2017</div>
    <p class="body-copy">Lorem ipsum dolor sit amet, consectetuer adipiscing elit, sed diam nonummy nibh euis mod tincidunt ut laoreet dolore magna ali quam erat volutpat.</p>
  </article>
</section>

<footer class="site-footer">
  <div class="notch"></div>
  <div class="footer-brand"><span class="dot"></span>Brightfold Pattern Works Collective</div>
  <div class="col" style="left:55px">
    <h4>Quick Links</h4>
    <ul><li>Home</li><li>Who We Are</li><li>What We Do</li><li>Expertise</li><li>News</li><li>Contact</li></ul>
  </div>
  <div class="col" style="left:233px">
    <h4>Contact</h4>
    <div class="contact-row"><svg viewBox="0 0 20 20"><path d="M10 1a6 6 0 0 0-6 6c0 5 6 12 6 12s6-7 6-12a6 6 0 0 0-6-6z" fill="none" stroke="#333" stroke-width="2"/><circle cx="10" cy="7" r="2" fill="#333"/></svg><span>Brightfold Pattern Works Collective<br>48 Harbor Grid Way<br>Miami, FL 33100</span></div>
    <div class="contact-row"><svg viewBox="0 0 20 20"><circle cx="10" cy="10" r="9" fill="none" stroke="#333" stroke-width="1.5"/><path d="M7 5h2l1 3-1.5 1c.5 1.5 1.5 2.5 3 3l1-1.5 3 1v2c-5 0-8.5-3.5-8.5-8.5z" fill="#333"/></svg><span>800-555-0147</span></div>
    <div class="contact-row"><svg viewBox="0 0 20 20"><circle cx="10" cy="10" r="9" fill="none" stroke="#333" stroke-width="1.5"/><rect x="5" y="7" width="10" height="7" fill="none" stroke="#333" stroke-width="1.5"/><path d="M5 7l5 4 5-4" fill="none" stroke="#333" stroke-width="1.5"/></svg><span>info@bpwcollective.com</span></div>
  </div>
  <div class="col" style="left:557px">
    <h4>Find Us</h4>
    <div class="map" role="img" aria-label="Street map showing the office location"></div>
  </div>
  <div class="col" style="left:892px">
    <h4>Newsletter</h4>
    <div class="signup"><span class="field">Enter Email Address</span><span class="go">SIGN UP</span></div>
  </div>
</footer>

<div class="bottom-bar">
  <span>COPYRIGHT © 2017 BRIGHTFOLD PATTERN WORKS COLLECTIVE. ALL RIGHTS RESERVED.</span>
  <span class="social"><span></span><span></span><span></span><span></span></span>
</div>

</body>
</html>
```